Modern and Clean Web Re-Design Project

We have 2 companies in similar industries: Printing and Mail Preparation/Fulfillment. We prefer sites that are clean and easy to navigate.Our printing company, Harbourline Press Works' website, hpwdirect.example is outdated needs revamping. We have rebranded our logo and are looking for a new design that is clean, modern and geared to other corporations and business in the downtown Toronto area. Our mailing company, The Postwick Depot (thepostwickdepot.example) needs a website as well. This company is in the Direct Mail and letter shop business, which essentially is addressing/personalizing people's printed matter and preparing it for either the Canadian or US postal service. The Postwick Depot specializes in not-for-profit and corporate sectors.Please see our logos to get an idea of the colors and look we want. For all intensive purposes, the sites can look similar in design all we want is that each site has the appropriate corporate colors and is a bit different so they don't look identical as the two business run as separate corporations.The content of the website should be easily changed by our staff and we want it to be setup to optimized for SEO based on the keywords we want. We are looking for someone to work on this project immediately
Updates

Project Deadline Extended
Reason: Change of ideas

After doing some thinking, I would like the site to be more modern but the non flash sites that I have seen so far Im finding life-less and while I want something clean, not overly busy and corporate looking, I dont want the design to be bland looking.

Please design with the previous specs in mind but with a twist as mentioned above.

Thanks
Dorian

Target Market(s)

See above

Industry/Entity Type

Printing

Requirements
Must have
• Must match the design and style of each respective logoSee the attached impage of the front of our offices to have an idea of our lookWe must be able to edit the content ourselves without any fancy programs or tools.Must be SEO optimized
Nice to have
• An online order form that can be emailed to us for quotes.....perhaps a page with a bunch of fields that have drop down menus....
Should not have
• Should not be overly busy. I want it to be clean and simple but informative without being hard to navigate

```html
<!DOCTYPE html>
<html lang="en">
<head>
<meta charset="utf-8">
<title>Harbourline Press Works</title>
<link rel="stylesheet" href="https://fonts.googleapis.com/css2?family=Source+Sans+3:wght@300;400&display=swap">
<style>
  :root {
    --ink: #231f20;
    --tab: #221e1f;
    --nav-text: #8c8a8a;
    --mid-grey: #8e8e8e;
    --light-grey: #e4e4e4;
    --white: #ffffff;
    --amber: #f9ae35;
    --slate: #6a6768;
    --brand-orange: #ee5a2f;
    --photo-a: #3a7f8a;
    --photo-b: #b9a46a;
    --photo-c: #6f8f4a;
  }
  * { margin: 0; padding: 0; box-sizing: border-box; }
  html, body { width: 1200px; height: 1101px; overflow: hidden; background: var(--white); }
  body { position: relative; font-family: "Source Sans 3", sans-serif; font-weight: 300; }

  .page {
    position: absolute; left: 121px; top: 67px; width: 943px; height: 972px;
    background: linear-gradient(to bottom, var(--ink) 0px, #2b2829 120px, #7a7a7a 220px, var(--mid-grey) 440px, #a9a9a9 700px, var(--light-grey) 900px);
  }

  .brand {
    position: absolute; left: 0; width: 100%; top: 90px; text-align: center;
    font-size: 24px; letter-spacing: 7px; text-transform: uppercase; color: var(--nav-text);
  }
  .brand-dot {
    display: inline-block; width: 14px; height: 14px; border-radius: 50%;
    background: var(--brand-orange); margin-right: 14px; vertical-align: 2px;
  }

  .main-nav a {
    position: absolute; top: 168px; height: 52px; background: var(--tab);
    color: var(--nav-text); text-decoration: none; font-size: 19px;
    text-align: right; padding: 14px 18px 0 0;
  }

  .slider {
    position: absolute; left: 9px; top: 221px; width: 922px; height: 320px;
    border: 4px solid var(--white);
  }
  .slide-photo {
    position: absolute; inset: 0;
    background: linear-gradient(100deg, var(--photo-a) 0%, #d8c9c4 22%, var(--photo-c) 45%, #e8eaea 62%, var(--photo-b) 82%, #8db0c2 100%);
  }
  .slide-title {
    position: absolute; left: 640px; top: 72px; font-size: 38px; font-weight: 400; color: var(--white);
  }
  .slide-text {
    position: absolute; left: 560px; top: 157px; width: 360px; font-size: 18px; line-height: 24px; color: var(--white);
  }
  .slider-dots { position: absolute; left: 0; top: 0; }

  .mission-title {
    position: absolute; left: 51px; top: 660px; font-size: 23px; font-weight: 400; color: var(--white);
  }
  .mission-rule {
    position: absolute; left: 271px; top: 675px; width: 340px; height: 1px; background: #c4c4c4;
  }
  .mission-text {
    position: absolute; left: 44px; top: 715px; width: 560px; font-size: 13px; line-height: 16.5px; color: var(--white);
  }

  .contact-card {
    position: absolute; left: 617px; top: 571px; width: 310px; height: 292px;
    background: var(--amber); border: 4px solid var(--white); color: var(--slate);
  }
  .contact-title { position: absolute; left: 45px; top: 65px; font-size: 23px; font-weight: 400; }
  .contact-address {
    position: absolute; right: 48px; top: 119px; text-align: right; font-size: 15px; line-height: 19.5px; text-transform: uppercase;
  }
  .contact-phone { position: absolute; right: 46px; top: 184px; font-size: 16px; font-weight: 400; letter-spacing: 1px; }
  .contact-email { position: absolute; right: 50px; top: 216px; font-size: 15px; }

  .site-footer {
    position: absolute; left: 0; top: 900px; width: 943px; height: 72px; background: var(--ink);
  }
  .footer-nav { position: absolute; left: 19px; top: 24px; font-size: 18px; color: var(--nav-text); }
  .footer-nav a { color: var(--nav-text); text-decoration: none; }
  .copyright { position: absolute; right: 33px; top: 20px; font-size: 22px; color: #5f5c5d; }
</style>
</head>
<body>
  <div class="page">
    <header>
      <div class="brand"><span class="brand-dot"></span>Harbourline Press Works</div>
      <nav class="main-nav">
        <a href="#" style="left:10px;width:231px;">WHO WE ARE</a>
        <a href="#" style="left:251px;width:211px;">WHAT WE DO</a>
        <a href="#" style="left:472px;width:222px;">EMAIL A FILE</a>
        <a href="#" style="left:701px;width:227px;">CONTACT US</a>
      </nav>
    </header>

    <section class="slider">
      <div class="slide-photo" role="img" aria-label="Photo of freshly printed colour posters hanging in rows"></div>
      <h2 class="slide-title">Digital Printing</h2>
      <p class="slide-text">HPW offers the latest technology available for photocopies, colour copies and poster printing.</p>
      <svg class="slider-dots" width="914" height="312" viewBox="0 0 914 312">
        <circle cx="727" cy="281" r="7.5" fill="#fff"/>
        <circle cx="759" cy="281" r="7.5" fill="#231f20"/>
        <circle cx="791" cy="281" r="7.5" fill="#fff"/>
        <circle cx="827" cy="281" r="7.5" fill="#fff"/>
        <circle cx="862" cy="281" r="7.5" fill="#fff"/>
      </svg>
    </section>

    <section>
      <h3 class="mission-title">MISSION STATEMENT</h3>
      <div class="mission-rule"></div>
      <p class="mission-text">We maintain absolute integrity in every aspect of our operation. By using our experience to understand our customers' expectations, we show an uncommon commitment to achieving a high-quality product under strict deadlines. It is the customers who set the standards we strive to achieve. We are professionals who bring unique and specialized skills you can depend on.</p>
    </section>

    <aside class="contact-card">
      <h3 class="contact-title">CONTACT US:</h3>
      <p class="contact-address">48 Larkspur Avenue East<br>Toronto, Ontario<br>M4K 2R9</p>
      <p class="contact-phone">416-555-0148</p>
      <p class="contact-email">ellis@hpwdirect.example</p>
    </aside>

    <footer class="site-footer">
      <nav class="footer-nav"><a href="#">WHO WE ARE</a> | <a href="#">WHAT WE DO</a> | <a href="#">EMAIL A FILE</a> | <a href="#">CONTACT US</a></nav>
      <p class="copyright">Copyright © hpwdirect.example</p>
    </footer>
  </div>
</body>
</html>
```